Web Design Job: Condo Debts Collection Business needs a Web Design

I need a site for a client, who works with condo debts collection, and ensure all revenues provided by condo fees will be always available to the building manager of condo on a specific date, regardless of defaults.
I have the visual identity (logo, slogan and colors) of the company, and some requirements on layout (kind of slider, menu options, phone number on a noble position, etc) - maybe I can do a sketch, but I like the idea of give some freedom to designer.

*** PLEASE, we have no interest in templates. We want something new***
Updates

Reason: We need something new, different and exclusive. We do not want anything that looks like a "template". Thanks.

Target Market(s)

I have two targets for this design:
- Condominium's building manager. This target is looking for a solution to overdue debts on it's condo.
- Residents on condominiums. This target wants to live in a better place, where their neighbors pay their condominium fees on time.

Industry/Entity Type

Business

Number of Pages Required

1 page

Requirements
Must have
• - Slider with title, some short text related, a nice image (I prefer happy and/or peaceful family, people doing business, happy friends, and so on).
• - I have a special attention to menu. I'm looking for one I can have a nice effect, more elegant, charming, kind of innovative.
• - Phone number on the top (or clearly visible).
• - Member log in area or icon on the top (or clearly visible).
• - News/articles area.
• - Modern fonts, with good quality, sans-serif on areas where reading is more intensive (prefer Google web-fonts).
• - Colors specified on attached files.
Nice to have
• - Clear background color, cause it's better to read larger texts (like articles). Dark backgrounds makes reading difficult.
• - A site with effects (like shadows, lines, curves, gradients, lights) is usually pretty.
• - I pay attention on beautiful footers.
Should not have
• - Images with a lot of money (I don't sell richness, I sell tranquility, peace, harmony, safety).
• - Poor menu.

```html
<!DOCTYPE html>
<html lang="pt">
<head>
<meta charset="utf-8">
<title>Condara Cobrança</title>
<link href="https://fonts.googleapis.com/css2?family=Open+Sans:wght@400;600;700;800&display=swap" rel="stylesheet">
<style>
:root{
  --navy:#1c2a5c;
  --navy-dark:#141f47;
  --orange:#ef6a1f;
  --text:#555b66;
  --muted:#8a8f99;
  --page:#f3f3f3;
  --band:#ececec;
  --footer:#a9abb0;
  --white:#ffffff;
}
*{margin:0;padding:0;box-sizing:border-box}
html,body{width:809px;height:1200px;overflow:hidden}
body{background:var(--page);font-family:"Open Sans",Arial,sans-serif;color:var(--text);position:relative}
.page{position:absolute;left:144px;top:0;width:520px;height:1090px;background:var(--white)}
.topbar{height:28px;background:var(--navy-dark);display:flex;justify-content:flex-end;align-items:center;gap:6px;padding-right:14px}
.topbar .social{width:12px;height:12px;background:#d6d9e2;border-radius:2px}
.header{height:78px;position:relative}
.brand{position:absolute;left:18px;top:10px;width:118px;height:58px;background:var(--navy);display:flex;align-items:center;gap:6px;padding:0 8px}
.brand .mark{width:10px;height:10px;background:var(--orange);flex:none}
.brand .name{color:var(--white);font-size:10px;font-weight:700;line-height:1.25}
.phones{position:absolute;right:18px;top:24px;text-align:right;font-size:9px;font-weight:700;color:var(--navy);line-height:1.5}
.phones svg{vertical-align:-1px;margin-right:3px}
.nav{height:22px;border-top:1px solid #e3e3e3;border-bottom:1px solid #e3e3e3;display:flex;align-items:center;padding:0 18px;font-size:7.5px;color:var(--muted)}
.nav a{margin-right:26px;text-decoration:none;color:var(--muted)}
.nav a.active{color:var(--orange);font-weight:700}
.search{margin-left:auto;width:96px;height:13px;border:1px solid #d8d8d8;font-size:6.5px;color:#aaa;padding:1px 5px;display:flex;align-items:center;justify-content:space-between}
.hero{position:relative;height:372px;overflow:hidden}
.hero .photo{position:absolute;inset:0;background:linear-gradient(135deg,#dfe4e8 0%,#c9d2d9 40%,#eef0f1 70%,#b9c2c9 100%)}
.slide-box{position:absolute;top:240px;width:136px;height:96px;background:var(--navy);color:var(--white);padding:10px 10px}
.slide-box h3{font-size:8px;font-weight:700;line-height:1.2;margin-bottom:6px;text-transform:uppercase}
.slide-box p{font-size:5.5px;line-height:1.45;color:#cfd4e3}
.box-a{left:218px}.box-b{left:374px}
.arrow{position:absolute;right:14px;top:268px}
.dots{position:absolute;left:36px;top:290px;display:flex;gap:4px}
.dots span{width:5px;height:5px;border-radius:50%;background:#fff;opacity:.7}
.dots span.on{background:var(--orange);opacity:1}
.hero .curve{position:absolute;left:0;bottom:0}
.intro{display:flex;gap:28px;padding:18px 34px 0}
.intro .col{flex:1;display:flex;gap:10px}
.intro svg{flex:none}
.intro h2{font-size:11px;font-weight:700;color:var(--navy);margin:4px 0 6px}
.intro p{font-size:6px;line-height:1.55}
.news-band{margin-top:30px;height:72px;background:var(--band);display:flex;flex-direction:column;align-items:center;justify-content:center;position:relative}
.news-band .title{display:flex;align-items:center;gap:8px}
.news-band h2{font-size:20px;font-weight:800;color:var(--navy)}
.news-band p{font-size:6px;color:var(--muted);margin-top:2px}
.news-band .notch{position:absolute;left:50%;bottom:-8px;transform:translateX(-50%)}
.news{display:grid;grid-template-columns:1fr 1fr;gap:26px 34px;padding:30px 34px 0}
.post h3{font-size:9px;font-weight:700;color:var(--orange);text-transform:uppercase}
.post .date{font-size:6px;color:var(--orange);margin:3px 0 7px;opacity:.8}
.post p{font-size:6px;line-height:1.55;margin-bottom:8px}
.btn{display:inline-block;background:var(--navy);color:var(--white);font-size:6px;font-weight:700;padding:4px 10px;border-radius:2px;text-transform:uppercase}
.footer{position:absolute;left:0;top:1090px;width:809px;height:110px;background:var(--footer);color:var(--white);text-align:center}
.footer nav{padding-top:22px;font-size:6.5px}
.footer nav a{color:var(--white);text-decoration:none;margin:0 12px}
.footer .legal{margin-top:12px;font-size:5.5px;line-height:1.6;opacity:.9}
</style>
</head>
<body>
<div class="page">
  <div class="topbar">
    <span class="social"></span><span class="social"></span><span class="social"></span><span class="social"></span>
  </div>
  <header class="header">
    <div class="brand"><span class="mark"></span><span class="name">Condara<br>Cobrança</span></div>
    <div class="phones">
      <div><svg width="7" height="7" viewBox="0 0 10 10"><path d="M2 1l2 2-1 1.5a6 6 0 0 0 2.5 2.5L7 6l2 2-1.5 1.5C4 9 1 6 .5 2z" fill="#1c2a5c"/></svg>(11) 4020-5566</div>
      <div>(11) 4020-7788</div>
    </div>
  </header>
  <nav class="nav">
    <a class="active">HOME</a><a>About Us</a><a>News</a><a>Services</a><a>Contact</a>
    <div class="search"><span>Search here...</span><svg width="6" height="6" viewBox="0 0 10 10"><circle cx="4" cy="4" r="3" fill="none" stroke="#999" stroke-width="1.5"/><path d="M6 6l3 3" stroke="#999" stroke-width="1.5"/></svg></div>
  </nav>
  <section class="hero">
    <div class="photo" role="img" aria-label="Photo of two smiling colleagues planning work with colourful sticky notes on a glass wall"></div>
    <div class="slide-box box-a"><h3>Vantagens de ser um cliente</h3><p>Receba a taxa do condomínio em dia, todos os meses, sem se preocupar com atrasos ou inadimplência dos moradores.</p></div>
    <div class="slide-box box-b"><h3>Vantagens de ser um cliente</h3><p>Tranquilidade para o síndico e harmonia entre vizinhos, com garantia de receita na data combinada.</p></div>
    <svg class="arrow" width="10" height="14" viewBox="0 0 10 14"><path d="M2 1l6 6-6 6" fill="none" stroke="#1c2a5c" stroke-width="2.5"/></svg>
    <div class="dots"><span class="on"></span><span></span><span></span></div>
    <svg class="curve" width="520" height="60" viewBox="0 0 520 60" preserveAspectRatio="none"><path d="M0 60 Q300 0 520 30 L520 60Z" fill="#ffffff"/></svg>
  </section>
  <section class="intro">
    <div class="col">
      <svg width="30" height="30" viewBox="0 0 30 30"><path d="M6 26h18M15 26V14M9 6l12 0-3 8h-6z" fill="none" stroke="#ef6a1f" stroke-width="2.5"/></svg>
      <div><h2>What about Condara</h2><p>Somos especialistas em cobrança condominial e garantimos que a receita das taxas esteja sempre disponível ao síndico na data certa. Trabalhamos com transparência, segurança e respeito a cada morador do condomínio.</p></div>
    </div>
    <div class="col">
      <svg width="30" height="30" viewBox="0 0 30 30"><circle cx="9" cy="9" r="4" fill="#ef6a1f"/><circle cx="21" cy="9" r="4" fill="#ef6a1f"/><path d="M2 24a7 7 0 0 1 14 0zM14 24a7 7 0 0 1 14 0z" fill="#ef6a1f"/></svg>
      <div><h2>Our services</h2><p>Oferecemos garantia de receita, gestão de inadimplência e acompanhamento jurídico completo. Assim o condomínio mantém suas contas em ordem e os vizinhos vivem em paz, com mais harmonia e tranquilidade no dia a dia.</p></div>
    </div>
  </section>
  <section class="news-band">
    <div class="title">
      <svg width="24" height="20" viewBox="0 0 24 20"><rect x="2" y="3" width="18" height="14" fill="none" stroke="#ef6a1f" stroke-width="2"/><path d="M5 7h12M5 10h12M5 13h8" stroke="#ef6a1f" stroke-width="1.5"/></svg>
      <h2>What's new ?</h2>
    </div>
    <p>Acompanhe as notícias do mundo condominial</p>
    <svg class="notch" width="16" height="8" viewBox="0 0 16 8"><path d="M0 0h16L8 8z" fill="#ececec"/></svg>
  </section>
  <section class="news">
    <article class="post"><h3>Condomínios inadimplentes?</h3><div class="date">12/03/2015</div><p>Saiba como a garantia de receita ajuda o síndico a manter as contas em dia, mesmo quando alguns moradores atrasam o pagamento das taxas mensais.</p><span class="btn">Read more</span></article>
    <article class="post"><h3>Condomínios inadimplentes?</h3><div class="date">08/03/2015</div><p>Conheça os direitos e deveres de cada condômino e entenda por que pagar em dia traz mais segurança e valorização ao seu imóvel.</p><span class="btn">Read more</span></article>
    <article class="post"><h3>Condomínios inadimplentes?</h3><div class="date">02/03/2015</div><p>Dicas práticas para reduzir atrasos, melhorar a comunicação com os moradores e planejar o orçamento anual do condomínio com tranquilidade.</p><span class="btn">Read more</span></article>
    <article class="post"><h3>Condomínios inadimplentes?</h3><div class="date">25/02/2015</div><p>Veja como funciona a cobrança amigável e por que ela preserva a boa convivência entre vizinhos enquanto resolve as dívidas pendentes.</p><span class="btn">Read more</span></article>
  </section>
</div>
<footer class="footer">
  <nav><a>Home</a><a>About Us</a><a>News</a><a>Services</a><a>Contact</a></nav>
  <div class="legal">Condara Cobrança Condominial<br>Rua das Palmeiras, 120 – São Paulo<br>(11) 4020-5566<br>Todos os direitos reservados</div>
</footer>
</body>
</html>
```